TEAL BEACON LICE REMOVAL labels

I need a label design for our MINT REPELLING SHAMPOO (LICE PREVENTION).
It also includes our MINT REPELLING CONDITIONER (LICE PREVENTION) and our MINT SPRAY (LICE PREVENTION) also includes LICE & NIT ELIMINATING MOUSSE (LICE TREATMENT) and a LICE ELIMINATOR 100% Dimethicone oil (LICE TREATMENT). The shampoo and conditioner are sulfate free, contains peppermint and other essential oils and is safe for the entire family. Label should be simple, modern and high end looking. Fun is good too if it looks nice!

Target Market(s)

Kids and Adults

Industry/Entity Type

Hair Care Product

Font styles to use
Sans Serif
Decorative

Requirements
Must have
• -Words that should be used: safe, non toxic, sulfate free, essential oils, pesticide free. - Naturally removes lice, super lice & nits are great words for the lice & nit eliminating mousse and treatment oil 100% Dimethicone oil
- On a side note there are no essential oils in the lice & nit eliminating mousse or treatment oil 100% Dimethicone oil
Nice to have
• Earth tone colors if possible
Kid safe, no fillers, colors or scents
100% effective (even against super lice)
8oz labels and 4oz labels
Should not have
• No pictures of lice

```html
<!DOCTYPE html>
<html lang="en">
<head>
<meta charset="utf-8">
<title>Teal Beacon Lice Removal – Mint Repelling Labels</title>
<link rel="stylesheet" href="https://fonts.googleapis.com/css2?family=Comfortaa:wght@400;700&display=swap">
<style>
  :root {
    --page-bg: #ffffff;
    --forest-dark: #2b3a1f;
    --forest-mid: #34452a;
    --label-light: #f4f4f4;
    --label-light-edge: #e6e6e6;
    --leaf-green: #3fa34d;
    --deep-green: #1f6b35;
    --wave-green: #23913f;
    --wave-olive: #6aa457;
    --wave-sage: #93b45e;
    --mint-light: #9fcf6a;
    --text-white: #ffffff;
    --logo-ink: #1f6b6b;
  }
  * { box-sizing: border-box; margin: 0; padding: 0; }
  html, body { width: 1200px; height: 1000px; overflow: hidden; background: var(--page-bg); }
  body { font-family: "Comfortaa", sans-serif; position: relative; }

  .label {
    position: absolute;
    top: 275px;
    width: 211px;
    height: 474px;
    overflow: hidden;
  }
  .label--shampoo { left: 367px; background: linear-gradient(90deg, var(--forest-dark), var(--forest-mid) 60%, var(--forest-dark)); }
  .label--conditioner { left: 597px; background: linear-gradient(90deg, var(--label-light-edge), var(--label-light) 40%, #fafafa 70%, var(--label-light-edge)); }

  .brand-badge {
    position: absolute;
    left: 58px;
    top: 48px;
    width: 106px;
    height: 106px;
    border-radius: 50%;
    background: #ffffff;
    display: flex;
    align-items: center;
    justify-content: center;
    text-align: center;
  }
  .label--conditioner .brand-badge { border: 1.5px solid #333; }
  .brand-name {
    font-size: 10px;
    font-weight: 700;
    line-height: 1.35;
    letter-spacing: 1.5px;
    color: var(--logo-ink);
  }

  .mint-sprig {
    position: absolute;
    left: 2px;
    top: 152px;
    width: 56px;
    height: 52px;
    border-radius: 50% 40% 50% 45%;
    background: radial-gradient(circle, rgba(120,190,90,0.35), rgba(120,190,90,0) 70%);
  }
  .mint-leaf-faint {
    position: absolute;
    right: -40px;
    top: 10px;
    width: 110px;
    height: 260px;
    border-radius: 50%;
    background: radial-gradient(ellipse, rgba(255,255,255,0.06), rgba(255,255,255,0) 70%);
  }
  .label--conditioner .mint-leaf-faint { background: radial-gradient(ellipse, rgba(0,0,0,0.05), rgba(0,0,0,0) 70%); }
  .label--conditioner .mint-sprig { background: radial-gradient(circle, rgba(120,190,90,0.2), rgba(120,190,90,0) 70%); }

  .product-copy {
    position: absolute;
    left: 45px;
    top: 187px;
  }
  .product-line { font-size: 17px; line-height: 20px; }
  .product-type { font-size: 17px; line-height: 20px; letter-spacing: 0.5px; }
  .claims { font-size: 8.6px; line-height: 11px; margin-top: 4px; font-weight: 700; }
  .claims .sep { font-weight: 400; }

  .label--shampoo .product-line { color: var(--text-white); }
  .label--shampoo .product-type { color: var(--leaf-green); }
  .label--shampoo .claims { color: var(--text-white); }
  .label--shampoo .claims .sep { color: var(--leaf-green); }

  .label--conditioner .product-line { color: var(--mint-light); }
  .label--conditioner .product-type { color: var(--deep-green); font-weight: 700; font-size: 15px; }
  .label--conditioner .claims { color: var(--leaf-green); }

  .volume {
    position: absolute;
    left: 75px;
    top: 382px;
    font-size: 8.5px;
    color: var(--mint-light);
    z-index: 2;
  }

  .waves { position: absolute; left: 0; bottom: 0; width: 211px; height: 102px; z-index: 1; }
</style>
</head>
<body>

<section class="label label--shampoo">
  <div class="mint-leaf-faint" role="img" aria-label="Faint mint leaf decoration"></div>
  <div class="brand-badge"><p class="brand-name">TEAL<br>BEACON<br>LICE<br>REMOVAL</p></div>
  <div class="mint-sprig" role="img" aria-label="Mint sprig illustration"></div>
  <div class="product-copy">
    <p class="product-line">Mint Repelling</p>
    <p class="product-type">SHAMPOO</p>
    <p class="claims">safe <span class="sep">|</span> non toxic <span class="sep">|</span> sulfate free<br>essential oils <span class="sep">|</span> pesticide free</p>
  </div>
  <p class="volume">100 ml &nbsp;| 6 OZ</p>
  <svg class="waves" viewBox="0 0 211 102" preserveAspectRatio="none">
    <path d="M70 56 C110 32 160 10 211 0 V102 H160 C140 85 105 66 70 56 Z" fill="var(--wave-olive)"/>
    <path d="M0 102 V20 C70 18 140 55 172 102 Z" fill="var(--wave-green)"/>
    <path d="M150 102 C172 86 193 68 211 54 V102 Z" fill="var(--wave-sage)"/>
  </svg>
</section>

<section class="label label--conditioner">
  <div class="mint-leaf-faint" role="img" aria-label="Faint mint leaf decoration"></div>
  <div class="brand-badge"><p class="brand-name">TEAL<br>BEACON<br>LICE<br>REMOVAL</p></div>
  <div class="mint-sprig" role="img" aria-label="Mint sprig illustration"></div>
  <div class="product-copy">
    <p class="product-line">Mint Repelling</p>
    <p class="product-type">CONDITIONER</p>
    <p class="claims">safe | non toxic | sulfate free<br>essential oils | pesticide free</p>
  </div>
  <p class="volume">100 ml &nbsp;| 6 OZ</p>
  <svg class="waves" viewBox="0 0 211 102" preserveAspectRatio="none">
    <path d="M70 56 C110 32 160 10 211 0 V102 H160 C140 85 105 66 70 56 Z" fill="var(--wave-olive)"/>
    <path d="M0 102 V20 C70 18 140 55 172 102 Z" fill="var(--wave-green)"/>
    <path d="M150 102 C172 86 193 68 211 54 V102 Z" fill="var(--wave-sage)"/>
  </svg>
</section>

</body>
</html>
```